Gazebrix fresh re-design

We are UK based company and have Magento website which we are happy with, but we require fresh design. Menu must be customer friendly

Design must reflect in strength as strength of our products and value for money are our selling points.

Our products are not family products there mainly used for business at events, cycling, running clubs, etc

New design must have same information as current design

links that require new design

http://www.gazebrix.example (landing page)

http://www.gazebrix.example/3m-x-3m-heavy-duty-tents/3m-x-3m-pop-up-marquee-white.html (product page)

http://www.gazebrix.example/custom-design-own-tent-size/choose-3mx3m.html (design tool)

Target Market(s)

business owners, cycling clubs, running clubs,

Industry/Entity Type

It Company

Number of Pages Required

3 page

Requirements
Must have
• background image of working gazebrix, clean fresh design, printed gazebrixes eg. cupcake
Should not have
• all same functions as current page

```html
<!DOCTYPE html>
<html lang="en">
<head>
<meta charset="utf-8">
<title>Gazebrix – Pop Up Marquees and Gazebos</title>
<link rel="stylesheet" href="https://fonts.googleapis.com/css2?family=Montserrat:wght@400;600;700&family=Great+Vibes&family=Arvo:wght@700&family=Arimo:wght@400&display=swap">
<style>
:root{
  --brand-red:#b3262b;
  --nav-blue:#14148c;
  --header-text:#3a3411;
  --meta-link:#8a4a14;
  --button-orange:#f3a51b;
  --button-yellow:#f7c531;
  --banner-blue:#1d1fa6;
  --banner-red:#d52424;
  --price-blue:#1a2a8c;
  --text:#3d3d3d;
  --page:#f7f7f7;
  --card-border:#e3e3e3;
  --footer:#2f2f2f;
  --footer-base:#262626;
  --footer-text:#e6e6e6;
}
*{box-sizing:border-box;margin:0;padding:0}
html,body{width:1092px;height:1200px;overflow:hidden}
body{position:relative;background:var(--page);font-family:"Montserrat",sans-serif;color:var(--text)}
.abs{position:absolute}
svg{display:block}

/* hero */
.hero-art{position:absolute;left:0;top:0;width:1092px;height:410px}
.brand{left:216px;top:20px;display:flex;align-items:center;gap:6px;font-weight:700;font-size:17px;color:var(--brand-red)}
.brand-mark{width:12px;height:12px;background:var(--brand-red)}
.meta-links{right:218px;top:6px;font-size:7.5px;color:var(--meta-link);display:flex;gap:8px}
.main-nav{left:398px;top:28px;display:flex;align-items:center;font-size:8.8px;font-weight:600;color:var(--header-text)}
.main-nav a{color:inherit;text-decoration:none;margin-right:26px}
.main-nav a.active{background:var(--nav-blue);color:#fff;padding:4px 6px;border-radius:2px;margin-right:22px}
.main-nav a:last-child{margin-right:0}
.cart{right:218px;top:55px;display:flex;align-items:center;gap:5px;font-size:7.5px;color:var(--header-text)}
.cart-count{background:var(--brand-red);color:#fff;padding:2px 6px}
.hero-title{left:218px;top:150px;font-size:23.5px;font-weight:700;line-height:27px;color:#fff}
.hero-title .script{font-family:"Great Vibes",cursive;font-weight:400;font-size:27px}
.hero-copy{left:218px;top:212px;width:312px;font-size:10.6px;line-height:16.5px;color:#fff}
.hero-button{left:220px;top:273px;width:152px;height:31px;background:linear-gradient(var(--button-yellow),var(--button-orange));border:1px solid #fff3;border-radius:2px;color:#fff;font-size:15px;display:flex;align-items:center;justify-content:center;gap:6px}
.hero-button .dot{width:13px;height:13px;border-radius:50%;background:#fff;display:flex;align-items:center;justify-content:center}

/* promo banners */
.promo-design{left:217px;top:456px;width:456px;height:94px;background:#f4f4f4;border:1px solid #ddd}
.promo-photo{position:absolute;left:0;top:0;width:196px;height:92px}
.promo-design .headline{position:absolute;left:252px;top:14px;font-family:"Arvo",serif;font-weight:700;font-size:16px;line-height:17px;color:#222}
.promo-design .headline small{font-size:14px}
.promo-design .headline b{color:var(--banner-red);display:block}
.promo-design .from{position:absolute;left:252px;top:60px;font-family:"Arvo",serif;font-weight:700;font-size:6.5px;color:var(--price-blue)}
.promo-design .price{position:absolute;left:284px;top:50px;font-family:"Arvo",serif;font-weight:700;font-size:28px;color:var(--price-blue)}
.promo-why{left:676px;top:455px;width:198px;height:96px;background:var(--banner-blue)}
.promo-why .headline{position:absolute;left:12px;top:8px;font-family:"Arvo",serif;font-weight:700;font-size:16px;line-height:16px;color:#fff}
.promo-why .sub{position:absolute;left:12px;top:44px;font-family:"Arvo",serif;font-weight:700;font-size:8px;line-height:10px;color:#fff}
.promo-why .sub em{font-style:normal;color:#9fe33a}
.promo-why .learn{position:absolute;left:12px;top:71px;width:74px;height:21px;background:var(--banner-red);color:#fff;font-size:7px;font-weight:700;display:flex;align-items:center;justify-content:center}
.promo-why .tent{position:absolute;right:0;top:12px;width:88px;height:84px}

/* intro */
.intro-title{left:217px;top:565px;width:657px;text-align:center;font-size:13px;font-weight:400;color:#555}
.intro-copy{left:217px;top:591px;width:657px;font-family:"Arimo",sans-serif;font-size:7.4px;line-height:15.4px;color:#444}
.divider{left:218px;top:660px;width:657px;height:6px;background:#e9e9e9}

/* featured */
.featured-title{left:217px;top:687px;width:657px;text-align:center;font-size:19px;font-weight:400;color:#222}
.featured-copy{left:261px;top:716px;width:570px;text-align:center;font-size:8.3px;line-height:11.5px;color:#555}
.card{width:152px;height:195px;top:765px;background:#fff;border:1px solid var(--card-border);overflow:hidden}
.card .photo{width:150px;height:141px}
.card .info{padding:5px 6px 0;font-size:9.3px;line-height:15.4px;color:#555}
.card.highlight{border-top:2px solid #f1d88a}
.card.highlight .photo{height:140px}
.arrow{top:840px;width:14px;height:34px;background:#e2e2e2;display:flex;align-items:center;justify-content:center}

/* footer */
.site-footer{left:0;top:998px;width:1092px;height:166px;background:var(--footer)}
.footer-base{left:0;top:1164px;width:1092px;height:36px;background:var(--footer-base)}
.footer-col h4{font-size:10.5px;font-weight:600;color:#fff;margin-bottom:8px}
.footer-col li{list-style:none;font-size:8.6px;line-height:15.4px;color:var(--footer-text);display:flex;align-items:center;gap:6px}
.social-icon{width:11px;height:11px;border-radius:2px}
.trust-badge{left:747px;top:1009px;width:90px;height:38px;background:#fff;border-radius:4px;border-bottom:5px solid #2d9a5e}
.copyright{left:191px;top:1175px;font-size:9px;color:#eee}
</style>
</head>
<body>

<svg class="hero-art" viewBox="0 0 1092 410" role="img" aria-label="Photo of pop-up gazebos set up at an outdoor event field, under a yellow header band">
  <defs>
    <linearGradient id="heroFill" x1="0" y1="0" x2="0" y2="1">
      <stop offset="0" stop-color="#dccd60"/>
      <stop offset="0.22" stop-color="#b9ad56"/>
      <stop offset="0.5" stop-color="#7f8a3e"/>
      <stop offset="0.8" stop-color="#8a6a47"/>
      <stop offset="1" stop-color="#6b5233"/>
    </linearGradient>
    <linearGradient id="heroShade" x1="0" y1="0" x2="1" y2="0">
      <stop offset="0" stop-color="#3a2e1a" stop-opacity="0.45"/>
      <stop offset="0.45" stop-color="#3a2e1a" stop-opacity="0.15"/>
      <stop offset="1" stop-color="#3a2e1a" stop-opacity="0.05"/>
    </linearGradient>
  </defs>
  <polygon points="0,0 1092,0 1092,351 607,403 0,356" fill="url(#heroFill)"/>
  <polygon points="0,90 546,66 1092,90 1092,351 607,403 0,356" fill="url(#heroShade)"/>
  <path d="M0,90 Q546,50 1092,90" fill="none" stroke="#e4d670" stroke-opacity="0.5"/>
</svg>

<div class="abs brand"><span class="brand-mark"></span>Gazebrix</div>
<div class="abs meta-links"><span>My Account</span><span>Sign In</span><span>View Cart</span></div>
<nav class="abs main-nav">
  <a class="active">Gazebrix</a><a>Roofs walls</a><a>Gazebo</a><a>Weights</a><a>Gutters</a><a>Sandbags</a><a>Tables</a><a>Parts</a>
</nav>
<div class="abs cart">
  <svg width="15" height="11" viewBox="0 0 15 11"><path d="M0 1h3l2 6h7l2-5H4" fill="none" stroke="#2a2a2a" stroke-width="1.4"/><circle cx="6" cy="9.5" r="1.2" fill="#2a2a2a"/><circle cx="11" cy="9.5" r="1.2" fill="#2a2a2a"/></svg>
  <span>Your Cart</span><span class="cart-count">0 item</span><span>$0.00</span>
</div>

<h1 class="abs hero-title">Where The <span class="script">Outdoors</span> Breathe<br>Indoor &amp; Time Stands Still</h1>
<p class="abs hero-copy">Gazebrix has built heavy duty pop-up gazebos for over 10 years, trusted by businesses, event teams and cycling and running clubs at great value.</p>
<div class="abs hero-button">Product Store <span class="dot"><svg width="7" height="7" viewBox="0 0 7 7"><path d="M2 1l3 2.5L2 6" fill="none" stroke="#f3a51b" stroke-width="1.5"/></svg></span></div>

<section class="abs promo-design">
  <svg class="promo-photo" viewBox="0 0 196 92" role="img" aria-label="Photo of two custom printed pop-up gazebos in red and green">
    <defs><linearGradient id="printed" x1="0" x2="1"><stop offset="0" stop-color="#b81e3c"/><stop offset="0.45" stop-color="#c0203f"/><stop offset="0.5" stop-color="#4aa83a"/><stop offset="1" stop-color="#5cbd3f"/></linearGradient></defs>
    <rect width="196" height="92" fill="#f2f2f2"/>
    <rect x="2" y="4" width="192" height="84" fill="url(#printed)"/>
  </svg>
  <div class="headline">DESIGN <small>your own</small><b>GAZEBRIX</b></div>
  <div class="from">FROM</div>
  <div class="price">€490</div>
</section>

<section class="abs promo-why">
  <div class="headline">WHY BUY<br>from us?</div>
  <div class="sub">Gazebrix provide<br>the <em>Cheapest prices</em></div>
  <div class="learn">LEARN MORE</div>
  <svg class="tent" viewBox="0 0 88 84" role="img" aria-label="Photo of an orange pop-up gazebo">
    <rect width="88" height="84" fill="#e8832a"/>
    <rect y="40" width="88" height="44" fill="#d06a1c"/>
  </svg>
</section>

<h2 class="abs intro-title">Pop Up Marquees and Gazebos for Sale</h2>
<p class="abs intro-copy">Mini Pop Up Marquees and Gazebos with sides<br>Pop up marquees / heavy duty gazebo for sale near you! We at gazebrixes have been able to expand our markets to different countries and our pop up marquees and heavy duty gazebos are now available for delivery in several European countries, so your wait is over. All you have to do now is order your instant awnings from our website gazebrix.example Please note we deliver to Ireland and all over Europe.</p>
<div class="abs divider"></div>

<h2 class="abs featured-title">Featured Product</h2>
<p class="abs featured-copy">Lorem Ipsum is simply dummy text of the printing and typesetting industry. Lorem Ipsum has been the industry's standard dummy text ever since the 1500s, when an unknown printer took a galley of type and scrambled it to make a type specimen book.</p>

<div class="abs arrow" style="left:195px"><svg width="6" height="9" viewBox="0 0 6 9"><path d="M5 1L1 4.5 5 8" fill="none" stroke="#777" stroke-width="1.3"/></svg></div>
<div class="abs arrow" style="left:883px"><svg width="6" height="9" viewBox="0 0 6 9"><path d="M1 1l4 3.5L1 8" fill="none" stroke="#777" stroke-width="1.3"/></svg></div>

<article class="abs card" style="left:219px">
  <svg class="photo" viewBox="0 0 150 141" preserveAspectRatio="none" role="img" aria-label="Photo of a white 3m x 3m pop-up gazebo on grass"><defs><linearGradient id="g1" x1="0" y1="0" x2="0" y2="1"><stop offset="0" stop-color="#3f4a36"/><stop offset="0.45" stop-color="#cfd2cc"/><stop offset="0.75" stop-color="#6f7d52"/><stop offset="1" stop-color="#fff"/></linearGradient></defs><rect width="150" height="141" fill="url(#g1)"/></svg>
  <div class="info">3m x 3m Heavy Duty Pop-Up<br>White<br>€449.00 ex vat</div>
</article>
<article class="abs card" style="left:386px">
  <svg class="photo" viewBox="0 0 150 141" preserveAspectRatio="none" role="img" aria-label="Photo of a yellow 15kg gazebo leg weight on grass"><defs><linearGradient id="g2" x1="0" y1="0" x2="0" y2="1"><stop offset="0" stop-color="#4f6a2c"/><stop offset="0.55" stop-color="#a8a640"/><stop offset="0.8" stop-color="#6c8a34"/><stop offset="1" stop-color="#fff"/></linearGradient></defs><rect width="150" height="141" fill="url(#g2)"/></svg>
  <div class="info">15kg Metal Weights<br>€65.00 ex vat</div>
</article>
<article class="abs card highlight" style="left:554px">
  <svg class="photo" viewBox="0 0 150 140" preserveAspectRatio="none" role="img" aria-label="Photo of an orange 3m x 3m pop-up gazebo on grass"><defs><linearGradient id="g3" x1="0" y1="0" x2="0" y2="1"><stop offset="0" stop-color="#39412f"/><stop offset="0.4" stop-color="#e58a2c"/><stop offset="0.75" stop-color="#5d6b3e"/><stop offset="1" stop-color="#fff"/></linearGradient></defs><rect width="150" height="140" fill="url(#g3)"/></svg>
  <div class="info">3m x 3m Heavy Duty Pop-Up<br>White<br>€449.00 ex vat</div>
</article>
<article class="abs card" style="left:722px">
  <svg class="photo" viewBox="0 0 150 141" preserveAspectRatio="none" role="img" aria-label="Photo of a white pop-up gazebo with side walls"><defs><linearGradient id="g4" x1="0" y1="0" x2="0" y2="1"><stop offset="0" stop-color="#8d9aa2"/><stop offset="0.5" stop-color="#e4e4e0"/><stop offset="0.8" stop-color="#7c8a5a"/><stop offset="1" stop-color="#fff"/></linearGradient></defs><rect width="150" height="141" fill="url(#g4)"/></svg>
  <div class="info">3m x 3m Heavy Duty Pop-Up<br>White<br>€449.00 ex vat</div>
</article>

<footer class="abs site-footer"></footer>
<div class="abs footer-base"></div>
<div class="abs footer-col" style="left:189px;top:1010px">
  <h4>Information</h4>
  <ul><li>About Us</li><li>FAQ</li><li>Instuctions</li><li>Contact us</li><li>Delivery, Payments and Returns</li><li>Blog</li><li>Log In</li></ul>
</div>
<div class="abs footer-col" style="left:406px;top:1010px">
  <h4>Our Services</h4>
  <ul><li>Printed Gazebrixes</li><li>Tenders</li><li>Tent Templates</li></ul>
</div>
<div class="abs footer-col" style="left:572px;top:1010px">
  <h4>Connect With Us</h4>
  <ul>
    <li><span class="social-icon" style="background:#3b5998"></span>Friendspace</li>
    <li><span class="social-icon" style="background:#3aa0d8"></span>Chirper</li>
    <li><span class="social-icon" style="background:#d8402c"></span>Circles +</li>
    <li><span class="social-icon" style="background:#d8312a"></span>Vidstream</li>
  </ul>
</div>
<div class="abs trust-badge" role="img" aria-label="Security certification badge"></div>
<p class="abs copyright">© 2014 Gazebrix TM. All Rights Reserved.</p>

</body>
</html>
```